Long Term Contract - Wordpress Designers Wanted!

We are rapidly growing start-up web development company, focused on website development geared towards the insurance industry.

To increase our impact, we’ve decided to add a freelance designer to the team to assist in graphical elements and webdesign for our clients and template development.

This is to screen for a LONG TERM relationship where we will work together to design and develop sites for insurance agents. We are seeking a talented web designer with experience in WordPress and WordPress theme development to work his/her magic on our new websites.

To win this contest, please create an example website design for an individual insurance agent that sells auto and home insurance. The website will essentially be a "business card" for the agent and will generate trust, show experience, and most importantly create a call to action for the person to call or get a quote.

An example is here:

http://plovermarsh.example/heron/

As part of the deliverable, we will want you to integrate these templates as child themes under Quillmorph "Trellis" template framework - which we can provide you of course. All forms should be done in gravity forms.

Target Market(s)

Audience: consumers shopping for insurance agent

Industry/Entity Type

Insurance

Requirements
Must have
• Pages:
-home
-products
-about
-news/blog
-Contact us

On home page the following elements should be included:
-contact us form
-agent contact information
-blog entries
-testimonial
-agency overview
Should not have
• flash

```html
<!DOCTYPE html>
<html lang="en">
<head>
<meta charset="utf-8">
<title>Company Name – Insurance Agent</title>
<link rel="stylesheet" href="https://fonts.googleapis.com/css2?family=Arimo:wght@400;700&family=Gelasio&family=Ubuntu:wght@400;500&family=Oswald:wght@500&display=swap">
<style>
:root{
  --page:#f3f1ee;
  --header:#ebe8e4;
  --text:#555;
  --dark:#444;
  --blue:#1547b8;
  --sky-top:#1f5fd0;
  --sky-bottom:#c9d9ef;
  --teal:#1e6e95;
  --field:#b3ada3;
  --footer:#b1aa9f;
  --footer-text:#fff;
  --line:#dedad4;
}
*{box-sizing:border-box;margin:0;padding:0}
html,body{width:866px;height:1200px;overflow:hidden}
body{position:relative;background:var(--page);font-family:"Arimo",Arial,sans-serif;color:var(--text)}
.abs{position:absolute}
.site-header{left:0;top:0;width:866px;height:89px;background:radial-gradient(ellipse at 130px 45px,#fff 0,var(--header) 130px)}
.brand{left:51px;top:31px;font-family:"Gelasio",Georgia,serif;font-size:22px;color:#444}
.phone{left:683px;top:33px;font-size:18px;color:#555;display:flex;align-items:center;gap:14px;font-family:"Ubuntu",sans-serif}
.main-nav{left:0;top:89px;width:866px;height:31px;background:linear-gradient(#f6f5f3,#e6e3df);border-top:1px solid #cfcac3;border-bottom:1px solid #cfcac3}
.main-nav a{position:absolute;top:0;height:30px;line-height:30px;font-size:12px;color:#555;text-decoration:none;padding:0 15px;border-right:1px solid #d8d4ce}
.main-nav a.active{background:#fff}
.search{left:694px;top:93px;width:146px;height:23px;border:1px solid #c8c3bc;border-radius:12px;background:#fff;overflow:hidden}
.search span{position:absolute;right:0;top:0;height:21px;width:64px;background:linear-gradient(#f7f6f4,#dedad5);border-left:1px solid #c8c3bc;font-size:11px;line-height:21px;text-align:center;color:#555}
.hero{left:0;top:120px;width:866px;height:265px;background:linear-gradient(170deg,var(--sky-top) 0,#4a83dc 45%,var(--sky-bottom) 100%)}
.hero-photo{left:500px;top:120px;width:366px;height:265px;background:radial-gradient(ellipse at 75% 40%,#e9b99a 0,rgba(233,185,154,.5) 30%,rgba(255,255,255,0) 60%)}
.hero-card{left:47px;top:200px;width:351px;height:154px;border:1px solid rgba(255,255,255,.45);border-radius:4px;background:rgba(40,90,190,.35)}
.hero-card p{position:absolute;left:14px;top:12px;width:330px;font-weight:700;font-size:10.5px;line-height:23px;color:#fff}
.btn-learn{left:14px;top:119px;width:92px;height:27px;background:linear-gradient(#2d86b0,#135e83);border:1px solid #0f4d6c;border-radius:3px;color:#fff;font-family:"Ubuntu",sans-serif;font-size:12px;line-height:25px;text-align:center}
.slide-tab{left:671px;top:362px;width:112px;height:23px;background:var(--page);border-radius:56px 56px 0 0}
.round{width:18px;height:18px;border-radius:50%;background:#fff;border:1px solid #d7d2cb;display:flex;align-items:center;justify-content:center}
.section-title{font-family:"Ubuntu",sans-serif;font-weight:400;color:#555}
.overview-title{left:56px;top:418px;font-size:16px}
.overview-icon{left:27px;top:418px;width:22px;height:22px}
.overview-text{left:27px;top:451px;width:512px;font-size:10px;line-height:14.6px;letter-spacing:.25px}
.overview-text p{margin-bottom:14.6px}
.news{left:27px;top:610px;width:528px;height:295px;background:#fff;border:1px solid #e0dcd6;border-radius:3px}
.news-title{left:14px;top:12px;font-size:17px}
.news-item{position:absolute;top:44px;width:242px}
.news-photo{height:86px;border:1px solid #e3e0db;padding:4px;background:#fff}
.news-photo div{width:100%;height:100%}
.news-item h3{margin-top:16px;font-family:"Ubuntu",sans-serif;font-weight:500;font-size:15px;color:#555}
.news-item p{margin-top:6px;font-size:10px;line-height:14.6px;width:245px;letter-spacing:.2px}
.btn-small{display:inline-block;margin-top:13px;padding:0 8px;height:24px;line-height:22px;border:1px solid #c5c0b8;border-radius:3px;background:linear-gradient(#fbfaf8,#e6e2dc);font-size:11px;color:#333}
.blog-title{left:576px;top:431px;font-family:"Oswald",sans-serif;font-size:15px;color:var(--blue);letter-spacing:.2px}
.blog-list{left:576px;top:459px;width:265px;border-top:1px solid var(--line)}
.blog-entry{padding:0 2px;font-size:9.6px;line-height:11.5px;color:#555;border-bottom:1px solid var(--line)}
.blog-entry em{display:block;font-size:9px;color:#777}
.contact-title{left:572px;top:687px;font-size:15px;font-weight:500}
.field{left:572px;width:252px;background:var(--field);border:1px solid #9c968c;border-radius:2px;color:#eee;font-size:10.5px;padding:14px 12px 0}
.btn-submit{left:755px;top:924px;width:70px;height:24px;border:1px solid #c5c0b8;border-radius:3px;background:linear-gradient(#fbfaf8,#e6e2dc);font-size:11px;line-height:22px;text-align:center;color:#333}
.site-footer{left:0;top:978px;width:866px;height:222px;background:var(--footer);border-top:1px solid #9f978b;color:var(--footer-text)}
.footer-heading{position:absolute;top:14px;font-family:"Oswald",sans-serif;font-size:20px;color:#fff;text-shadow:0 1px 1px rgba(0,0,0,.25)}
.footer-text{position:absolute;font-size:9.6px;line-height:14.6px}
.btn-footer{position:absolute;top:140px;width:65px;height:20px;background:#f4f2ee;border:1px solid #cfc9bf;font-size:8px;line-height:18px;text-align:center;color:#333}
.social{position:absolute;left:638px;top:58px;font-size:10px;font-family:"Ubuntu",sans-serif}
.social li{list-style:none;height:21px;display:flex;align-items:center;gap:13px}
.social i{width:12px;height:12px;background:#e9eef5;border:1px solid #8aa0bf;display:block}
.footer-bottom{position:absolute;left:28px;top:175px;width:813px;border-top:1px solid #a59e92;padding-top:18px;font-size:9px;display:flex;justify-content:space-between}
.footer-bottom nav a{color:#fff;text-decoration:none;margin-left:18px}
</style>
</head>
<body>
<header class="abs site-header">
  <div class="abs brand">Company Name</div>
  <div class="abs phone">
    <svg width="18" height="14" viewBox="0 0 18 14" aria-hidden="true"><path d="M1 4 Q9 -1 17 4 L15 6 L12 5 L12 3 Q9 2 6 3 L6 5 L3 6 Z" fill="#444"/><rect x="4" y="7" width="10" height="7" rx="1" fill="#444"/><circle cx="9" cy="10.5" r="1.8" fill="#ebe8e4"/></svg>
    555.302.7184
  </div>
</header>
<nav class="abs main-nav">
  <a style="left:31px">Home</a>
  <a class="active" style="left:96px">Company</a>
  <a style="left:177px">Markets</a>
  <a style="left:251px">Products &amp; Services</a>
  <a style="left:388px">Partners</a>
  <a style="left:465px">Careers</a>
  <a style="left:538px">News &amp; Events</a>
</nav>
<div class="abs search"><span>Search</span></div>

<section class="abs hero"></section>
<div class="abs hero-photo" role="img" aria-label="Hand holding a padlock and keys against a cloudy sky"></div>
<div class="abs hero-card">
  <p>Loremipsum dopor Loremipsum dopor Loremipsum dopor Loremipsum doporLoremipsum dopor Loremipsum dopor-Loremipsum dopor Loremipsum doporLoremipsum dopor Loremipsumsum dopor</p>
  <div class="abs btn-learn">Learn More</div>
</div>
<div class="abs slide-tab">
  <div class="abs round" style="left:28px;top:6px"><svg width="8" height="6"><path d="M1 1 L4 4 L7 1" stroke="#1a3f9c" stroke-width="2" fill="none"/></svg></div>
  <div class="abs" style="left:57px;top:7px;width:1px;height:14px;background:#ccc"></div>
  <div class="abs round" style="left:68px;top:6px"><svg width="8" height="6"><path d="M1 5 L4 2 L7 5" stroke="#1a3f9c" stroke-width="2" fill="none"/></svg></div>
</div>

<svg class="abs overview-icon" viewBox="0 0 22 22" aria-hidden="true"><path d="M3 17 L15 5 L18 8 L6 20 Z" fill="#e8a23a"/><path d="M5 4 L19 18" stroke="#c0392b" stroke-width="3"/></svg>
<h2 class="abs section-title overview-title">Agency Overview</h2>
<div class="abs overview-text">
  <p>Praesent varius faucibus nibh, nec imperdiet metus semper id. sent laoreet, leo quis gravida pretiuunc ipsum accumsan mi, sit ametique arcu massa sed mi. Semper dolor. Nullam tincidunt posuere laoreet. Cras et gravida nunc. Duis pharetra porttitor neque, tristique venenatis elit viverra rhoncus. Mauris tincidunt porta suscipit.</p>
  <p>Duis pharetra porttitor neque, tristique venenatis elit viverra rhoncus. Mauris tincidunt porta suscipit. Praesent varius faucibus nibh, nec imperdiet metus semper id.</p>
  <p>sent laoreet, leo quis gravida pretiuunc ipsum accumsan mi, sit ametique arcu massa sed mi. Semper dolor. Nullam tincidunt posuere laoreet. Cras et gravida nunc.</p>
</div>

<section class="abs news">
  <h2 class="abs section-title news-title">Latest News &amp; Events</h2>
  <div class="abs round" style="left:474px;top:10px;width:20px;height:20px"><svg width="6" height="8"><path d="M5 1 L2 4 L5 7" stroke="#1a3f9c" stroke-width="2" fill="none"/></svg></div>
  <div class="abs round" style="left:503px;top:10px;width:20px;height:20px"><svg width="6" height="8"><path d="M1 1 L4 4 L1 7" stroke="#1a3f9c" stroke-width="2" fill="none"/></svg></div>
  <article class="news-item" style="left:12px">
    <div class="news-photo"><div role="img" aria-label="Office desk phone beside a computer screen" style="background:linear-gradient(100deg,#d9d9d9,#8a8a8a 55%,#c7ccd6)"></div></div>
    <h3>Heading 1</h3>
    <p>Praesent varius faucibus nibh, nec imperdiet metus semper id. sent laoreet, leo quis gravida pretiuunc ipsum accumsan mi, sit ametique arcu massa sed mi. Semper dolor. sit ametique arcu massa sed mi. Semper dolor.</p>
    <span class="btn-small">Read More</span>
  </article>
  <article class="news-item" style="left:276px">
    <div class="news-photo"><div role="img" aria-label="Business team meeting in an office" style="background:linear-gradient(100deg,#8e9aa6,#c9b8a6 40%,#6d7c8c 75%,#3a3f47)"></div></div>
    <h3>Heading 2</h3>
    <p>Praesent varius faucibus nibh, nec imperdiet metus semper id. sent laoreet, leo quis gravida pretiuunc ipsum accumsan mi, sit ametique arcu massa sed mi. Semper dolor. sit ametique arcu massa sed mi. Semper dolor.</p>
    <span class="btn-small">Read More</span>
  </article>
</section>

<h2 class="abs blog-title">BLOG ENTRIES</h2>
<div class="abs blog-list">
  <div class="blog-entry" style="padding-top:23px;height:67px">A nice shot of my upcoming landing page design for the new project at lorest nest mixum alticit allet.<em>2 days ago</em></div>
  <div class="blog-entry" style="padding-top:18px;height:63px">A nice shot of my upcoming landing page design for the new project at lorest nest mixum alticit allet.<em>2 days ago</em></div>
  <div class="blog-entry" style="padding-top:22px;border-bottom:0">A nice shot of my upcoming landing page design for the new project at lorest nest mixum alticit allet.<em>2 days ago</em></div>
</div>

<h2 class="abs section-title contact-title">Contact Us</h2>
<div class="abs field" style="top:717px;height:35px">email*</div>
<div class="abs field" style="top:766px;height:35px;padding-top:11px">name*</div>
<div class="abs field" style="top:814px;height:89px;padding-top:10px">message*</div>
<div class="abs btn-submit">Submit</div>

<footer class="abs site-footer">
  <h2 class="footer-heading" style="left:28px">Agent Contact Information</h2>
  <div class="footer-text" style="left:28px;top:57px">Address Line 1<br>Address Line 2<br>Phone no. : +113 2468 9753<br>Email :</div>
  <div class="btn-footer" style="left:213px">READ MORE</div>
  <h2 class="footer-heading" style="left:334px">Testimonial</h2>
  <div class="footer-text" style="left:334px;top:51px;width:235px">Lorem ipsum dolor sit ipsum Lorem ipsum dolor sit ipsumLorem ipsum dolor sit ipsum</div>
  <div class="abs" style="left:334px;top:86px;width:218px;border-top:1px dashed #eee"></div>
  <div class="footer-text" style="left:334px;top:95px;width:235px">Lorem ipsum dolor sit ipsum Lorem ipsum dolor sit ipsumLorem ipsum dolor sit ipsum</div>
  <div class="btn-footer" style="left:520px">READ MORE</div>
  <h2 class="footer-heading" style="left:638px">Get Social with Us</h2>
  <ul class="social">
    <li><i></i>Like me on Friendbook</li>
    <li><i></i>Follow me on Chirper</li>
    <li><i></i>Get in touch by Mail</li>
    <li><i></i>My ProLinker profile</li>
  </ul>
  <div class="footer-bottom">
    <span>© 2012Company Name | All Rights Reserved</span>
    <nav><a>Company</a><a>Markets</a><a>Products &amp; Services</a><a>Partners</a><a>Careers</a><a>News &amp; Events</a></nav>
  </div>
</footer>
</body>
</html>
```